WordPress Blog/Website for Athlete Focused Sports Marketing Agency

WordPress Website that Serves two primary purposes:

1) Company Information Website which showcases organization's capabilities and work

2) Highlights, Showcases and Displays key information for athlete clients, aggregates all of the content they are creating(mostly social) and is a key portal for publishing press releases, news updates and more.

Key Criteria for Success:

Easily Updatable
Easy to Navigate
Clean Design that follows the function/form of the organization's brand identity while also incorporating the identity of the athletes.

Supporting Documentation:**These files are also uploaded and attached to this project description**
Creative Brief: https://files.briskhollow.net/a/lanternmoor.com/file/d/7KxR2mTqWvB9pLnYcHsDfJgZaQe/edit?usp=sharing
Logo Files/Designs are attached. Color Palette can be adjusted as necessary.

WireFrame: (Please use your own judgement and creative liberty's to make something that is a lot better then what I came up with):
https://files.briskhollow.net/file/d/7KxR2mTqWvB9pXtNbVcMwQrLsKy/edit?usp=sharing

Current Website(Incomplete): www.lanternmoor.com

Thanks!

Industry/Entity Type

It Company

Requirements
Must have
• Social Media Integration: A social feed that aggregates content across all channels for multiple users(all of my athletes)

"News=Blog" Portal that serves as the primary engine for the page's content

Professional Look and Design- it should look like a website, not a blog.

```html
<!DOCTYPE html>
<html lang="en">
<head>
<meta charset="utf-8">
<title>Lantern &amp; Moor</title>
<link rel="stylesheet" href="https://fonts.googleapis.com/css2?family=Arimo:wght@400;700&family=Crimson+Text:wght@400;600&display=swap">
<style>
:root{
  --orange:#f07d10;
  --orange-dark:#e26a00;
  --text:#4a4a4a;
  --line:#dcdcdc;
  --panel:#efefef;
  --bg:#fafafa;
  --footer-grey:#9a9a9a;
}
*{box-sizing:border-box;margin:0;padding:0}
html,body{width:802px;height:1200px;overflow:hidden}
body{background:var(--bg);font-family:"Arimo",Arial,sans-serif;color:var(--text);position:relative}
a{color:inherit;text-decoration:none}
.abs{position:absolute}

.brand{left:60px;top:64px;font-size:20px;font-weight:700;color:var(--orange);line-height:24px}

.search{left:566px;top:66px;width:113px;height:19px;border:1px solid #ccc;background:#fff;font-size:8px;padding:5px 8px;color:#333}
.search svg{position:absolute;right:5px;top:4px}
.lang{left:686px;top:66px;width:57px;height:19px;border:1px solid #ccc;background:#fff;font-size:7.5px;padding:5px 0 0 22px;color:#333}
.lang .flag{position:absolute;left:7px;top:6px;width:11px;height:7px;background:#2d3f86;border:1px solid #c33}
.lang svg{position:absolute;right:7px;top:7px}

.nav{left:60px;top:111px;width:682px;height:34px;background:linear-gradient(#fca13a,var(--orange-dark));display:flex;border:1px solid #e06a00}
.nav a{color:#fff;font-size:8.5px;font-weight:700;line-height:32px;padding:0 17px;border-right:1px solid #ffb35a}
.social{right:0;top:6px;display:flex;gap:9px;position:absolute;padding-right:7px}
.social span{width:21px;height:21px;border-radius:50%;background:#fff}

.slider{left:60px;top:150px;width:682px;height:223px;background:#d6d6d6;padding:7px 6px}
.slide-photo{width:100%;height:209px;background:linear-gradient(100deg,#1f5fa6,#3c86cf 55%,#2a6db5)}
.news-box{left:85px;top:180px;width:266px;height:166px;background:rgba(12,24,40,.92);color:#fff;padding:13px 12px}
.news-box h2{font-size:13.5px;font-weight:700;letter-spacing:.3px;padding-bottom:8px;border-bottom:1px solid #4a5668}
.news-box h3{font-size:11.5px;font-weight:700;line-height:17px;margin-top:10px}
.news-box p{font-size:8.5px;line-height:15px;color:#d7dbe2;margin-top:7px;text-align:justify}
.news-box .meta{font-size:8.5px;color:#a9b2be;margin-top:6px}
.dots{left:659px;top:335px;display:flex;gap:6px}
.dots span{width:10px;height:10px;border-radius:50%;border:2px solid #fff;background:#7fa3cc}
.dots span:first-child{background:#fff}

.content{left:60px;top:385px;width:682px;height:700px;background:#fff;border:1px solid var(--line)}
.section-title{left:10px;top:15px;font-family:"Crimson Text",Georgia,serif;font-weight:400;font-size:16px;color:var(--orange)}
.intro{left:10px;top:42px;width:662px;font-size:8.7px;line-height:15.5px;color:#555}

.card{width:202px}
.card .photo{width:202px;height:136px;border:3px solid #d3d3d3}
.card h4{font-family:"Crimson Text",Georgia,serif;font-weight:400;font-size:12.5px;color:var(--orange);margin:14px 0 0 2px}
.card p{font-size:8.7px;line-height:14px;margin:4px 2px 0;color:#555;text-align:justify}
.card .row{font-size:8.7px;margin:6px 2px 0;color:#555}
.card .row a{color:var(--orange)}
.card .files{margin-top:7px;height:30px;background:var(--panel);display:flex;align-items:center;gap:20px;padding-left:13px;font-size:9.5px;color:#333}
.card .files span{display:flex;align-items:center;gap:9px}

.pager{left:307px;top:1055px;display:flex;gap:3px;align-items:center}
.pager span{width:15px;height:14px;background:#d5d5d5;color:#fff;font-size:6.5px;text-align:center;line-height:14px;border-radius:2px}
.pager span.on{background:#888}
.pager i{font-style:normal;font-size:7px;color:#888;padding:0 3px}

.foot-links{left:59px;top:1103px;font-size:9.3px;color:#444}
.foot-links b{font-weight:400;margin:0 7px}
.copy{left:59px;top:1125px;font-size:9.3px;color:#444}
.foot-brand{right:60px;top:1110px;font-size:13px;font-weight:700;color:var(--footer-grey)}
</style>
</head>
<body>

<header>
  <div class="abs brand">Lantern &amp; Moor</div>
  <div class="abs search">Search
    <svg width="11" height="11" viewBox="0 0 11 11"><circle cx="4.5" cy="4.5" r="3.3" fill="none" stroke="#222" stroke-width="1.6"/><path d="M7 7l3 3" stroke="#222" stroke-width="2"/></svg>
  </div>
  <div class="abs lang"><span class="flag"></span>Eng
    <svg width="6" height="4" viewBox="0 0 6 4"><path d="M0 0h6L3 4z" fill="#333"/></svg>
  </div>
  <nav class="abs nav">
    <a href="#">HOME</a><a href="#">WHAT WE DO</a><a href="#">ATHLETES</a><a href="#">NEWS</a><a href="#">CONTACT US</a>
    <div class="social"><span></span><span></span><span></span></div>
  </nav>
</header>

<section class="abs slider">
  <div class="slide-photo" role="img" aria-label="Cyclist in red jersey drinking from a bottle against a blue sky"></div>
</section>
<article class="abs news-box">
  <h2>LATEST NEWS</h2>
  <h3>Sed placerat arcu quis arcu semper, nec tincidunt nibh molestie</h3>
  <p>Interdum et malesuada fames ac ante ipsum primis in faucibus. Aliquam gravida at nisi eu tempor. In sit amet nisi in augue cursus faucibus.</p>
  <div class="meta">Jun-17-2013 &nbsp;| &nbsp; Category : Tournament</div>
</article>
<div class="abs dots"><span></span><span></span><span></span><span></span></div>

<main class="abs content">
  <h1 class="abs section-title">Athletes</h1>
  <p class="abs intro">Lantern and Moor Media Group is the agency of the 21st century. &nbsp; Combining critical thought, industry expertise, strategic thinking and a results driven process, L&amp;M is emerging as a leading full service agency for consulting, strategic partnerships, business development, lifestyle marketing, media planning, athlete representation, event sponsorship and more. &nbsp; From Lantern Avenue to Moor Avenue, L&amp;M is a credible voice and thought leader that can move any brand forward.</p>

  <div class="abs card" style="left:10px;top:103px">
    <div class="photo" role="img" aria-label="Athlete doing push-ups on grass" style="background:linear-gradient(160deg,#b9c98a,#7fa44a 60%,#5f8a2e)"></div>
    <h4>Athlete Brand Building</h4>
    <p>Mauris varius mi tortor, eget commodo augue dignissim at. Aenean imperdiet.</p>
    <div class="row">Website : <a href="#">www.sitename.com</a></div>
    <div class="row">Event : July 2 Cras a turpis nec tellus suscipit</div>
    <div class="files"><span><svg width="15" height="17" viewBox="0 0 15 17"><path d="M1 .5h9l4 4v12H1z" fill="#fff" stroke="#c9302c"/><rect x="1" y="10" width="10" height="5" fill="#d9342b"/></svg>Media Guide</span><span><svg width="15" height="17" viewBox="0 0 15 17"><path d="M1 .5h9l4 4v12H1z" fill="#fff" stroke="#c9302c"/><rect x="1" y="10" width="10" height="5" fill="#d9342b"/></svg>Brand Book</span></div>
  </div>
  <div class="abs card" style="left:239px;top:103px">
    <div class="photo" role="img" aria-label="Hurdler clearing a hurdle under a sunny sky" style="background:linear-gradient(160deg,#2f6fc0,#5b9be0 50%,#3a7ccb)"></div>
    <h4>Athlete Brand Building</h4>
    <p>Mauris varius mi tortor, eget commodo augue dignissim at. Aenean imperdiet.</p>
    <div class="row">Website : <a href="#">www.sitename.com</a></div>
    <div class="row">Event : July 2 Cras a turpis nec tellus suscipit</div>
    <div class="files"><span><svg width="15" height="17" viewBox="0 0 15 17"><path d="M1 .5h9l4 4v12H1z" fill="#fff" stroke="#c9302c"/><rect x="1" y="10" width="10" height="5" fill="#d9342b"/></svg>Media Guide</span><span><svg width="15" height="17" viewBox="0 0 15 17"><path d="M1 .5h9l4 4v12H1z" fill="#fff" stroke="#c9302c"/><rect x="1" y="10" width="10" height="5" fill="#d9342b"/></svg>Brand Book</span></div>
  </div>
  <div class="abs card" style="left:467px;top:103px">
    <div class="photo" role="img" aria-label="Woman running along a beach boardwalk" style="background:linear-gradient(180deg,#bfd3e6,#e3e6e4 65%,#c7b89c)"></div>
    <h4>Athlete Brand Building</h4>
    <p>Mauris varius mi tortor, eget commodo augue dignissim at. Aenean imperdiet.</p>
    <div class="row">Website : <a href="#">www.sitename.com</a></div>
    <div class="row">Event : July 2 Cras a turpis nec tellus suscipit</div>
    <div class="files"><span><svg width="15" height="17" viewBox="0 0 15 17"><path d="M1 .5h9l4 4v12H1z" fill="#fff" stroke="#c9302c"/><rect x="1" y="10" width="10" height="5" fill="#d9342b"/></svg>Media Guide</span><span><svg width="15" height="17" viewBox="0 0 15 17"><path d="M1 .5h9l4 4v12H1z" fill="#fff" stroke="#c9302c"/><rect x="1" y="10" width="10" height="5" fill="#d9342b"/></svg>Brand Book</span></div>
  </div>

  <div class="abs card" style="left:10px;top:390px">
    <div class="photo" role="img" aria-label="Two runners jogging side by side against a blue sky" style="background:linear-gradient(160deg,#6fc3ec,#3ba6de 60%,#2b8fcb)"></div>
    <h4>Athlete Brand Building</h4>
    <p>Mauris varius mi tortor, eget commodo augue dignissim at. Aenean imperdiet.</p>
    <div class="row">Website : <a href="#">www.sitename.com</a></div>
    <div class="row">Event : July 2 Cras a turpis nec tellus suscipit</div>
    <div class="files"><span><svg width="15" height="17" viewBox="0 0 15 17"><path d="M1 .5h9l4 4v12H1z" fill="#fff" stroke="#c9302c"/><rect x="1" y="10" width="10" height="5" fill="#d9342b"/></svg>Media Guide</span><span><svg width="15" height="17" viewBox="0 0 15 17"><path d="M1 .5h9l4 4v12H1z" fill="#fff" stroke="#c9302c"/><rect x="1" y="10" width="10" height="5" fill="#d9342b"/></svg>Brand Book</span></div>
  </div>
  <div class="abs card" style="left:239px;top:390px">
    <div class="photo" role="img" aria-label="Sprinter breaking the finish tape in a stadium" style="background:linear-gradient(180deg,#c99a94,#d8b1a6 55%,#7aa05a 78%,#c2623e)"></div>
    <h4>Athlete Brand Building</h4>
    <p>Mauris varius mi tortor, eget commodo augue dignissim at. Aenean imperdiet.</p>
    <div class="row">Website : <a href="#">www.sitename.com</a></div>
    <div class="row">Event : July 2 Cras a turpis nec tellus suscipit</div>
    <div class="files"><span><svg width="15" height="17" viewBox="0 0 15 17"><path d="M1 .5h9l4 4v12H1z" fill="#fff" stroke="#c9302c"/><rect x="1" y="10" width="10" height="5" fill="#d9342b"/></svg>Media Guide</span><span><svg width="15" height="17" viewBox="0 0 15 17"><path d="M1 .5h9l4 4v12H1z" fill="#fff" stroke="#c9302c"/><rect x="1" y="10" width="10" height="5" fill="#d9342b"/></svg>Brand Book</span></div>
  </div>
  <div class="abs card" style="left:467px;top:390px">
    <div class="photo" role="img" aria-label="Woman in pink jacket running through a forest" style="background:linear-gradient(120deg,#4a3a32,#8a6a55 50%,#5a4a40)"></div>
    <h4>Athlete Brand Building</h4>
    <p>Mauris varius mi tortor, eget commodo augue dignissim at. Aenean imperdiet.</p>
    <div class="row">Website : <a href="#">www.sitename.com</a></div>
    <div class="row">Event : July 2 Cras a turpis nec tellus suscipit</div>
    <div class="files"><span><svg width="15" height="17" viewBox="0 0 15 17"><path d="M1 .5h9l4 4v12H1z" fill="#fff" stroke="#c9302c"/><rect x="1" y="10" width="10" height="5" fill="#d9342b"/></svg>Media Guide</span><span><svg width="15" height="17" viewBox="0 0 15 17"><path d="M1 .5h9l4 4v12H1z" fill="#fff" stroke="#c9302c"/><rect x="1" y="10" width="10" height="5" fill="#d9342b"/></svg>Brand Book</span></div>
  </div>
</main>

<nav class="abs pager">
  <span class="on">1</span><span>2</span><span>3</span><span>4</span><span>5</span><span>6</span><span>7</span><span>8</span><span>»</span><i>···</i><span>»»</span>
</nav>

<footer>
  <div class="abs foot-links">Home<b>|</b>What we do<b>|</b>Athletes<b>|</b>News<b>|</b>Contact Us</div>
  <div class="abs copy">Copyright &nbsp;© &nbsp;2013 &nbsp;&nbsp; www.lanternmoor.com &nbsp;&nbsp; All rights reserved.</div>
  <div class="abs foot-brand">Lantern &amp; Moor</div>
</footer>

</body>
</html>
```